Modern, Bright Bubble Bath Label

We need a label design for a private label bubble bath we will begin selling.

We will have 8 different scents of bubble bath. Each has a color associated with it as follows: Napa Valley Grape (Purple), Mixed Berry (Blue), Bartlett Pear (Green), Sweet Pineapple (Yellow), Juicy Peach (Orange), Red Raspberry (Red), Creamy Coconut (Brown or White), Kiwi Watermelon (Pink). So what we want is 8 different bottle labels. The labels CAN be different, but they will likely be the same label, just with a different color and different text (scent name).

Labels should be bright, fun, modern, and clean. The main color should be what is listed above, but other colors can be incorporated, as can be seen in the attachments.

Label should be between 2.5" and 3.5" tall, and 7.25" wide. This will be applied to an 8oz boston round, plastic, transparent bottle with a black cap.

For reference, I love The Fern Parlor packaging designs.

Target Market(s)

Women

Industry/Entity Type

Hair And Beauty

Logo Text

Amber Cove

Font styles to use
Serif
Sans Serif

Requirements
Must have
• -Company Logo: 'Amber Cove', which will need to be designed by the winning designer. You can simply put 'Amber Cove' in the label for now as a place holder.
• -Text 'Glimmering Foam Bath'
• -Name of Scent
• -Packaging that is brightly colored and associated with the scent as mentioned in the product description.
• Should be in format that can be edited in Adobe Photoshop. We will add additional text and details (ingredients, description, etc.) in Photoshop once we choose the winning design
Nice to have
• Picture or graphic of associated fruit

```html
<!DOCTYPE html>
<html lang="en">
<head>
<meta charset="utf-8">
<title>Amber Cove – Napa Valley Grape Label</title>
<link rel="stylesheet" href="https://fonts.googleapis.com/css2?family=Kaushan+Script&display=swap">
<style>
  :root {
    --page: #ffffff;
    --grape-deep: #6e1a55;
    --grape-mid: #5d2a6e;
    --dusk: #3f5a92;
    --lagoon: #0d86b6;
    --sky: #08aee8;
    --panel: #ffffff;
    --plum-text: #6a1d55;
    --berry-text: #a0397a;
    --fruit-light: #b0508c;
    --fruit: #a13d7f;
  }
  * { margin: 0; padding: 0; box-sizing: border-box; }
  html, body {
    width: 1200px;
    height: 1000px;
    overflow: hidden;
    background: var(--page);
  }
  .canvas {
    position: relative;
    width: 1200px;
    height: 1000px;
  }
  .label {
    position: absolute;
    left: 381px;
    top: 47px;
    width: 438px;
    height: 906px;
    background: linear-gradient(180deg,
      var(--grape-deep) 0%,
      var(--grape-mid) 35%,
      var(--dusk) 52%,
      var(--lagoon) 70%,
      var(--lagoon) 85%,
      var(--sky) 100%);
  }
  .label__panel {
    position: absolute;
    left: 85px;
    top: 160px;
    width: 270px;
    height: 588px;
    background: var(--panel);
  }
  .brand-name {
    position: absolute;
    left: 0;
    right: 0;
    top: 68px;
    text-align: center;
    font-family: "Kaushan Script", cursive;
    font-weight: 400;
    font-size: 38px;
    line-height: 1.2;
    color: var(--plum-text);
  }
  .fruit-art {
    position: absolute;
    left: 78px;
    top: 210px;
    width: 115px;
    height: 137px;
    background: linear-gradient(180deg, var(--fruit-light) 0%, var(--fruit) 100%);
  }
  .scent-name {
    position: absolute;
    left: 0;
    right: 0;
    top: 380px;
    text-align: center;
    font-family: "Kaushan Script", cursive;
    font-weight: 400;
    font-size: 25px;
    line-height: 1.2;
    color: var(--plum-text);
  }
  .product-type {
    position: absolute;
    left: 0;
    right: 0;
    top: 522px;
    text-align: center;
    font-family: "Kaushan Script", cursive;
    font-weight: 400;
    font-size: 24px;
    line-height: 1.2;
    color: var(--berry-text);
  }
</style>
</head>
<body>
  <main class="canvas">
    <section class="label" role="img" aria-label="Label background: purple to blue gradient where a flowing splash pattern belongs">
      <div class="label__panel">
        <p class="brand-name">Amber Cove</p>
        <div class="fruit-art" role="img" aria-label="Placeholder for a grape bunch illustration"></div>
        <p class="scent-name">Napa Valley Grape</p>
        <p class="product-type">Glimmering Foam Bath</p>
      </div>
    </section>
  </main>
</body>
</html>
```